Business card for marketing analytics company

Need a business card for new company. I have a logo already that I want to be built into the card and should use those colours

Company is called Larkfield Insight
Design must bring Larkfield Insight to life not be a card that could be for anyone with a logo put on it.

Like the front to be fairly clean and uncluttered bringing the logo out with a suitable design on the back of the card.

The logo represents a compass and business growth so those themes along with numbers, analytics , data are appropriate.
I'm often working with creative industries so also needs to reflect the creative side of analytics rather than be very corporate looking.

Target Market(s)

Ad agency, media agency, consumer goods clients

Industry/Entity Type

Market Research

Contact Information for Business Card

Needs to include name, title, email and phone number

Colors
f78f20
f68d4d
ec1f27

Requirements
Must have
• Must bring Larkfield Insight to life not be a card that could be for anyone with a logo put on it.
• Logo, Correct colours
• Like a design on the back that relates to company name
• Designs for both sides
Should not have
• Please do not just submit logo and a coloured card.
• It needs to have a design element to it
• No black background
• No clear cards - needs front & back

```html
<!DOCTYPE html>
<html lang="en">
<head>
<meta charset="utf-8">
<title>Larkfield Insight – Business Card</title>
<link rel="stylesheet" href="https://fonts.googleapis.com/css2?family=Open+Sans:wght@400;600;700&display=swap">
<style>
  :root {
    --backdrop: #ecebe8;
    --card-white: #ffffff;
    --slate: #535d66;
    --slate-dark: #3f474e;
    --orange: #f47a20;
    --orange-deep: #d9661a;
    --red: #c1242b;
    --red-deep: #9c1b21;
    --ink-grey: #5a6068;
    --ring-red: #c9302c;
  }
  html, body {
    margin: 0;
    padding: 0;
    width: 1200px;
    height: 1016px;
    overflow: hidden;
    background: var(--backdrop);
    font-family: "Open Sans", Arial, sans-serif;
  }
  .canvas {
    position: relative;
    width: 1200px;
    height: 1016px;
  }
  .card {
    position: absolute;
    left: 250px;
    width: 700px;
    height: 400px;
    background: var(--card-white);
    box-shadow: 0 10px 28px rgba(0, 0, 0, 0.16);
    overflow: hidden;
  }
  .card--front { top: 64px; }
  .card--back  { top: 552px; }

  /* Front side */
  .front-brand {
    position: absolute;
    inset: 0;
    display: flex;
    flex-direction: column;
    align-items: center;
    justify-content: center;
    gap: 26px;
  }
  .front-brand__ring {
    width: 120px;
    height: 120px;
    border-radius: 50%;
    border: 8px solid var(--ring-red);
    box-sizing: border-box;
  }
  .front-brand__name {
    margin: 0;
    font-weight: 700;
    font-size: 52px;
    line-height: 1;
    color: var(--ink-grey);
  }

  /* Back side */
  .back-art {
    position: absolute;
    inset: 0;
    width: 700px;
    height: 400px;
  }
  .contact-name  { font-size: 26px; font-weight: 400; fill: var(--ink-grey); }
  .contact-phone { font-size: 23px; font-weight: 600; fill: #ffffff; }
  .contact-email { font-size: 19px; font-weight: 400; fill: #ffffff; }

  .back-brand {
    position: absolute;
    right: 52px;
    bottom: 40px;
    display: flex;
    align-items: center;
    gap: 12px;
  }
  .back-brand__ring {
    width: 40px;
    height: 40px;
    border-radius: 50%;
    border: 3px solid #ffffff;
    box-sizing: border-box;
  }
  .back-brand__name {
    margin: 0;
    font-weight: 600;
    font-size: 24px;
    color: #ffffff;
  }
</style>
</head>
<body>
<main class="canvas">

  <section class="card card--front" aria-label="Card front">
    <div class="front-brand">
      <div class="front-brand__ring"></div>
      <p class="front-brand__name">Larkfield Insight</p>
    </div>
  </section>

  <section class="card card--back" aria-label="Card back">
    <svg class="back-art" viewBox="0 0 700 400" xmlns="http://www.w3.org/2000/svg">
      <polygon class="band band--orange" points="0,170 70,135 260,235 700,10 700,52 260,277 70,177 0,212" fill="var(--orange)" stroke="var(--orange-deep)" stroke-width="2"/>
      <polygon class="band band--red" points="0,213 70,178 260,278 700,53 700,94 260,319 70,219 0,254" fill="var(--red)" stroke="var(--red-deep)" stroke-width="2"/>
      <polygon class="band band--slate" points="0,256 70,221 260,321 700,96 700,400 0,400" fill="var(--slate)" stroke="var(--slate-dark)" stroke-width="3"/>

      <g class="contact" transform="translate(260 235) rotate(-27.08)">
        <text class="contact-name" x="34" y="-9">Sam Carter CEO</text>
        <text class="contact-phone" x="26" y="28">0207 555 0192</text>
        <text class="contact-email" x="22" y="65">samcarter@larkfieldinsight.com</text>
      </g>
    </svg>

    <div class="back-brand">
      <div class="back-brand__ring"></div>
      <p class="back-brand__name">Larkfield Insight</p>
    </div>
  </section>

</main>
</body>
</html>
```